Web Design For Metal Recycling Company

We are a scrap and recycling company dealing mainly in scrap metal base in Singapore. We deal in both domestic market and international market. Currently we are still unsure if we want to have a "lively" or "professional" company image so we will leave it to the designer to deem what is good.

We wish for a website to be able to "Retain" the interest of new visitor and at the same time able to give enough information for new and existing customer. We would also wish for design that will get the visitor to "Engage" us.

The attached is the logo for the company and we would want to incorporate that into the website. Either of the logo is fine.

```html
<!DOCTYPE html>
<html lang="en">
<head>
<meta charset="utf-8">
<title>Kai Teck Metal Recycling</title>
<link href="https://fonts.googleapis.com/css2?family=Cabin:wght@400;500;600&family=Open+Sans:ital,wght@0,400;0,600;1,400;1,600&display=swap" rel="stylesheet">
<style>
  :root {
    --gold: #c9942a;
    --gold-dark: #b07f1c;
    --navy: #3c3b7d;
    --navy-dark: #33326c;
    --ink: #333333;
    --muted: #7a7a7a;
    --soft-bg: #efefef;
    --tab-bg: #f5f4ea;
    --copy-bg: #2d2d2d;
    --white: #ffffff;
  }
  * { box-sizing: border-box; margin: 0; padding: 0; }
  html, body { width: 949px; height: 1200px; overflow: hidden; }
  body { position: relative; background: var(--white); font-family: "Open Sans", Arial, sans-serif; color: var(--ink); }
  .abs { position: absolute; }

  /* header */
  .site-header { position: absolute; left: 0; top: 0; width: 949px; height: 85px; background: var(--white); }
  .brand { left: 127px; top: 8px; width: 150px; text-align: center; }
  .brand-mark { display: block; width: 40px; height: 40px; margin: 0 auto 6px; border: 3px solid var(--gold); }
  .brand-name { font-family: "Cabin", sans-serif; font-weight: 600; font-size: 14px; color: var(--gold); letter-spacing: .5px; line-height: 1.1; }
  .main-nav { left: 433px; top: 0; height: 85px; display: flex; }
  .main-nav a { display: flex; align-items: center; height: 85px; padding: 0 8px; margin-right: 6px; font-family: "Cabin", sans-serif; font-size: 14px; color: #6f6f6f; text-decoration: none; }
  .main-nav a::after { content: ""; width: 5px; height: 5px; border-right: 1.2px solid currentColor; border-bottom: 1.2px solid currentColor; transform: rotate(45deg); margin: -3px 0 0 6px; }
  .main-nav a.active { color: var(--navy); border-bottom: 3px solid var(--gold); padding-top: 3px; }
  .search-icon { left: 805px; top: 53px; }

  /* hero */
  .hero { left: 0; top: 85px; width: 949px; height: 272px; background: radial-gradient(ellipse at 60% 40%, #6b6b6b 0%, #3b3b3b 45%, #1e1e1e 100%); }
  .contact-card { left: 201px; top: 123px; width: 236px; }
  .contact-card .title-band { background: var(--gold); height: 58px; text-align: center; color: var(--white); padding-top: 5px; }
  .contact-card h2 { font-family: "Cabin", sans-serif; font-weight: 500; font-size: 26px; line-height: 1.2; }
  .contact-card p { font-size: 11px; }
  .field { position: absolute; left: 6px; width: 230px; height: 33px; background: rgba(255,255,255,.25); padding: 3px 6px; }
  .field span { display: block; background: #f4f4f4; height: 27px; line-height: 27px; padding-left: 7px; font-size: 12px; color: #555; }
  .submit-btn { left: 90px; top: 158px; width: 61px; height: 23px; background: var(--gold); color: var(--white); font-size: 11px; font-weight: 600; line-height: 23px; text-align: center; }

  /* tabs */
  .tab-bar { left: 0; top: 357px; width: 949px; height: 33px; background: var(--tab-bg); }
  .tab { position: absolute; top: 0; height: 33px; display: flex; align-items: center; justify-content: center; gap: 9px; font-size: 12px; color: #444; border-right: 2px solid #e3e0cf; }
  .tab.active { background: var(--navy); color: var(--white); border-right: none; }

  /* feature row */
  .feature { top: 408px; width: 172px; }
  .feature h3 { display: flex; align-items: center; gap: 5px; font-family: "Cabin", sans-serif; font-weight: 500; font-size: 14px; color: #222; height: 32px; }
  .feature p { font-size: 10.5px; line-height: 1.45; color: var(--muted); margin-top: 2px; }

  /* about */
  .about-band { left: 0; top: 505px; width: 949px; height: 247px; background: var(--soft-bg); }
  .about { left: 121px; top: 528px; width: 160px; }
  .about h3 { font-family: "Cabin", sans-serif; font-weight: 400; font-size: 15px; color: var(--gold); margin: 0 0 6px 3px; }
  .about p { font-style: italic; font-size: 10px; line-height: 1.4; color: #666; margin-bottom: 14px; }
  .about a { font-size: 10.5px; color: var(--navy); text-decoration: none; }
  .pillar { top: 528px; width: 165px; height: 203px; background: var(--navy); text-align: center; color: var(--white); padding-top: 18px; }
  .pillar h4 { font-family: "Cabin", sans-serif; font-weight: 500; font-size: 18px; letter-spacing: 1px; color: var(--gold); margin: 2px 0 6px; }
  .pillar p { font-size: 10.5px; line-height: 1.45; padding: 0 18px; }

  /* services */
  .service { top: 822px; width: 172px; }
  .service .icon { height: 50px; display: flex; align-items: center; justify-content: center; width: 120px; }
  .service h3 { font-family: "Cabin", sans-serif; font-weight: 400; font-size: 15.5px; color: var(--gold); margin-top: 23px; }
  .service p { font-size: 10.5px; line-height: 1.45; color: #666; margin-top: 2px; }

  /* footer */
  .site-footer { left: 0; top: 1004px; width: 949px; height: 110px; background: var(--navy); color: var(--white); }
  .footer-links { left: 99px; top: 18px; font-size: 10.5px; }
  .footer-links a { color: var(--white); text-decoration: none; }
  .footer-links .sep { margin: 0 4px; }
  .footer-heading { font-family: "Cabin", sans-serif; font-style: italic; font-size: 15px; color: #c9c9e6; }
  .subscribe { left: 434px; top: 14px; }
  .subscribe-form { display: flex; margin-top: 10px; }
  .subscribe-form .input { width: 145px; height: 22px; background: #f4f4f4; color: #999; font-style: italic; font-size: 11px; line-height: 22px; padding-left: 8px; }
  .subscribe-form .go { width: 30px; height: 22px; background: var(--gold); display: flex; align-items: center; justify-content: center; }
  .social { display: flex; gap: 6px; margin: 8px 0 0 41px; }
  .social span { width: 21px; height: 21px; border: 1.5px solid var(--white); border-radius: 50%; }
  .address { left: 719px; top: 14px; width: 150px; }
  .address p { font-size: 9.5px; color: #b9b9da; line-height: 1.4; margin-top: 8px; }

  .map { left: 0; top: 1114px; width: 949px; height: 60px; background: linear-gradient(90deg, #8fa1ad 0%, #c9c7b4 45%, #d9d5c4 60%, #9fb0b9 100%); }
  .map-btn { left: 435px; top: 1145px; width: 79px; height: 21px; background: #f5f5f0; display: flex; align-items: center; justify-content: center; gap: 5px; font-size: 10.5px; color: #333; }
  .copyright { left: 0; top: 1174px; width: 949px; height: 26px; background: var(--copy-bg); color: var(--white); font-size: 10.5px; line-height: 26px; padding-left: 122px; }
</style>
</head>
<body>

<header class="site-header">
  <div class="abs brand">
    <span class="brand-mark"></span>
    <div class="brand-name">KAI TECK METAL RECYCLING</div>
  </div>
  <nav class="abs main-nav">
    <a class="active">Home</a><a>Products</a><a>Services</a><a>Locations</a><a>Contact Us</a>
  </nav>
  <svg class="abs search-icon" width="16" height="16" viewBox="0 0 16 16"><circle cx="6.5" cy="6.5" r="5" fill="none" stroke="#555" stroke-width="2.2"/><path d="M10.3 10.3 14.5 14.5" stroke="#555" stroke-width="2.6" stroke-linecap="round"/></svg>
</header>

<section class="abs hero" role="img" aria-label="Black and white photograph of a pile of scrap metal pipes and bars"></section>

<form class="abs contact-card">
  <div class="title-band">
    <h2>Contact Us:</h2>
    <p>Itaque earum rerum hic tenetur a sapiente.</p>
  </div>
  <div class="field" style="top:68px"><span>Your name</span></div>
  <div class="field" style="top:110px"><span>Email address</span></div>
  <div class="abs submit-btn">Submit</div>
</form>

<div class="abs tab-bar">
  <div class="tab" style="left:208px;width:122px">
    <svg width="13" height="13" viewBox="0 0 14 14"><circle cx="7" cy="7" r="4.5" fill="none" stroke="var(--gold)" stroke-width="3" stroke-dasharray="2.2 1.3"/><circle cx="7" cy="7" r="2.4" fill="var(--gold)"/></svg>Ferrous Scrap</div>
  <div class="tab" style="left:330px;width:151px">
    <svg width="9" height="15" viewBox="0 0 9 15"><path d="M2 1h5L3 7h4L2 14" fill="none" stroke="var(--gold)" stroke-width="2"/></svg>Non-Ferrous Scrap</div>
  <div class="tab" style="left:481px;width:156px">
    <svg width="13" height="13" viewBox="0 0 14 14"><circle cx="7" cy="7" r="6" fill="none" stroke="var(--gold)" stroke-width="1.6"/><path d="M5.5 4v6l4.5-3z" fill="var(--gold)"/></svg>Recycling Process</div>
  <div class="tab active" style="left:637px;width:112px">
    <svg width="15" height="11" viewBox="0 0 15 11"><rect width="15" height="11" fill="var(--gold)"/><path d="M0 1l7.5 5L15 1" fill="none" stroke="var(--navy)" stroke-width="1.3"/></svg>Contact us</div>
</div>

<div class="abs feature" style="left:121px">
  <h3><svg width="22" height="30" viewBox="0 0 22 30"><rect x="1" y="2" width="20" height="4" rx="1" fill="var(--gold)"/><path d="M3 7h16l-2 22H5z" fill="var(--gold)"/><path d="M8 10v16M11 10v16M14 10v16" stroke="#fff" stroke-width="1"/></svg>FERROUS SCRAP</h3>
  <p>Nemo enim ipsam voluptatem quia voluptas sit aspernatur aut odit aut fugit, sed quia consequuntur.</p>
</div>
<div class="abs feature" style="left:301px">
  <h3><svg width="22" height="30" viewBox="0 0 22 30"><rect x="7" y="1" width="8" height="5" fill="var(--gold)"/><path d="M6 6h10l5 8v15H1V14z" fill="var(--gold)"/></svg>NON-FERROUS SCRAP</h3>
  <p>Itaque earum rerum hic tenetur a sapiente delectus, ut aut reiciendis voluptatibus maiores alias.</p>
</div>
<div class="abs feature" style="left:481px">
  <h3><svg width="28" height="30" viewBox="0 0 28 30"><rect x="1" y="5" width="20" height="24" rx="4" fill="var(--gold)"/><rect x="5" y="10" width="12" height="7" fill="#fff"/><rect x="23" y="2" width="3" height="16" fill="var(--gold)"/></svg>USED MACHINERY</h3>
  <p>Duis aute irure dolor in reprehenrit in voluptate velit esse cillum dolore eu fugiat nulla pariatur.</p>
</div>
<div class="abs feature" style="left:661px">
  <h3><svg width="28" height="30" viewBox="0 0 28 30"><path d="M4 28h14M8 28l4-12 10-8" fill="none" stroke="var(--gold)" stroke-width="3.5"/><circle cx="22" cy="7" r="3.5" fill="var(--gold)"/><path d="M2 6h10" stroke="var(--gold)" stroke-width="3"/></svg>REROLLABLE SCRAP</h3>
  <p>Perspiciatis unde omnis iste natus error sit voluptatem accusantium doloremque laudantium.</p>
</div>

<div class="abs about-band"></div>
<div class="abs about">
  <h3>About Us</h3>
  <p>Nemo enim ipsam voluptatem quia voluptas sit aspernatur aut odit aut fugit, sed quia .</p>
  <p>Ut enim ad minima veniam, quis nostrum exercitationem ullam corporis suscipit laboriosam.</p>
  <p>Quis autem vel eum iure reprehenderit qui in ea voluptate velit esse quam.</p>
  <a>Read More &nbsp;›</a>
</div>

<div class="abs pillar" style="left:301px">
  <svg width="48" height="48" viewBox="0 0 48 48"><path d="M24 6a18 18 0 1 1-17 12" fill="none" stroke="#fff" stroke-width="7"/><path d="M2 12l10-6 2 12z" fill="#fff"/></svg>
  <h4>REUSE</h4>
  <p>Temporibus autem quibusdam et aut officiis debitis aut rerum necessitatibus saepe eveniet ut et voluptates .</p>
</div>
<div class="abs pillar" style="left:481px">
  <svg width="48" height="48" viewBox="0 0 48 48" fill="#fff"><path d="M6 6l12 12M42 6L30 18M6 42l12-12M42 42L30 30" stroke="#fff" stroke-width="5"/><path d="M20 10v10H10zM28 10v10h10zM20 38V28H10zM28 38V28h10z"/></svg>
  <h4>REDUCE</h4>
  <p>Temporibus autem quibusdam et aut officiis debitis aut rerum necessitatibus saepe eveniet ut et voluptates .</p>
</div>
<div class="abs pillar" style="left:662px">
  <svg width="48" height="48" viewBox="0 0 48 48" fill="none" stroke="#fff" stroke-width="6"><path d="M17 12l7-8 7 8M8 30l-4 9h12M40 30l4 9H32"/></svg>
  <h4>RECYCLE</h4>
  <p>Temporibus autem quibusdam et aut officiis debitis aut rerum necessitatibus saepe eveniet ut et voluptates .</p>
</div>

<div class="abs service" style="left:121px">
  <div class="icon"><svg width="70" height="44" viewBox="0 0 70 44" fill="none" stroke="#444" stroke-width="3"><path d="M4 10l14-6 16 8 16-8 16 6-8 18-18 10L12 26z"/></svg></div>
  <h3>Our Business</h3>
  <p>Lorem ipsum dolor sit amet, consectetur adipisicing elit, sed do eiusmod tempor incididunt.</p>
</div>
<div class="abs service" style="left:301px">
  <div class="icon"><svg width="60" height="46" viewBox="0 0 60 46" fill="none" stroke="#444" stroke-width="3"><path d="M4 24h52l-8 14H12z"/><path d="M14 24V12h16v12M20 12V3"/><path d="M2 43h56"/></svg></div>
  <h3>Cargo Stuffing</h3>
  <p>Duis aute irure dolor in reprehenderit in voluptate velit esse cillum dolore eu fugiat.</p>
</div>
<div class="abs service" style="left:481px">
  <div class="icon"><svg width="50" height="50" viewBox="0 0 50 50"><circle cx="25" cy="25" r="19" fill="none" stroke="#444" stroke-width="7" stroke-dasharray="5 3"/><circle cx="25" cy="25" r="9" fill="none" stroke="#444" stroke-width="4"/></svg></div>
  <h3>Breaking and Cutting</h3>
  <p>Excepteur sint occaecat cupidatat non proident, sunt in culpa qui officia deserunt mollit anim.</p>
</div>
<div class="abs service" style="left:661px">
  <div class="icon"><svg width="56" height="46" viewBox="0 0 56 46" fill="none" stroke="#444" stroke-width="3"><rect x="20" y="4" width="33" height="28" rx="3"/><path d="M20 14H10l-7 10v12h17"/><circle cx="12" cy="37" r="5"/><circle cx="42" cy="37" r="5"/></svg></div>
  <h3>Transport services</h3>
  <p>Quis autem vel eum iure reprehenderit qui in ea voluptate velit esse.</p>
</div>

<footer class="abs site-footer">
  <div class="abs footer-links"><a>Home</a><span class="sep">|</span><a>About Us</a><span class="sep">|</span><a>Careers</a><span class="sep">|</span><a>Contact Us</a><span class="sep">|</span><a>Services</a></div>
  <div class="abs subscribe">
    <div class="footer-heading">Subscribe</div>
    <div class="subscribe-form">
      <div class="input">Enter your E-mail</div>
      <div class="go"><svg width="12" height="9" viewBox="0 0 15 11"><rect width="15" height="11" fill="#fff"/><path d="M0 1l7.5 5L15 1" fill="none" stroke="var(--gold)" stroke-width="1.5"/></svg></div>
    </div>
    <div class="social"><span></span><span></span><span></span><span></span></div>
  </div>
  <div class="abs address">
    <div class="footer-heading">Address</div>
    <p>114 , Sunt in culpa qui officia deserunt mollitia anim.</p>
  </div>
</footer>

<div class="abs map" role="img" aria-label="Street map of the company location"></div>
<div class="abs map-btn"><svg width="9" height="12" viewBox="0 0 9 12"><path d="M4.5 12C1 7 0 6 0 4.5a4.5 4.5 0 0 1 9 0C9 6 8 7 4.5 12z" fill="var(--gold)"/><circle cx="4.5" cy="4.5" r="1.6" fill="#fff"/></svg>View Map</div>
<div class="abs copyright">copyright © 2014</div>

</body>
</html>
```